"Tallow Mouthguards " Custom-made Mouthguard Business Website

We need an informational website for our mouthguard Business "Tallow Mouthguards". The logo is navy blue/lime green so want to have colour scheme that goes nicely with this - have uploaded our mouthguard flyer with some information we need to put into the website but I do have more information to put in there.

Target Market(s)

Sports clubs, sportspeople, parents and kids, schools

Industry/Entity Type

Dental, Custom-made Sports Mouthguards

Coding

Number of Pages Required

5+ page

Font styles to use
Serif
Sans Serif

Colors
0054AA
0677BA
7BADD7
CADEEF
E8F1F8
0094D4
00A9DD
6FCCEA
C7EBF8
E9F6FB
00AB8E
00BBA5
67D7C9
C6EFE9
E9F9F6
59FF00
82FF00
B8FF75
E3FFCB
F4FFEA
FFF300
FFF600
FEFA6F
FFFEC7
FFFEE8
FFC000
F8CF3A
FAE287
FDF2CF
FEFAEE
F0912C
F2A743
F7CA91
FBE8D2
FDF5EE
EE7325
F08F49
F5BC92
FAE3D3
FDF4ED

Requirements
Must have
• I want drop down pages, not one scrolling page. Different pages for each heading . Content uploaded - We need a general home page with lots of pictures and info that I'll provide. A page each dedicated to 1) About Us 2) Why choose a custom mouthguard? 3) Gallery 4) Contact Us. Will need logos from "Morvex"
Nice to have
• Mainly use greens and blues, but happy to pop in some yellow/oranges/red oranges if it looks good

```html
<!DOCTYPE html>
<html lang="en">
<head>
<meta charset="utf-8">
<title>Tallow Mouthguards – Custom-Made Sports Mouthguards in Perth</title>
<link rel="stylesheet" href="https://fonts.googleapis.com/css2?family=Ubuntu:ital,wght@0,400;0,500;0,700;1,400&display=swap">
<style>
:root{
  --navy:#1f36a8;
  --navy-deep:#2236b0;
  --green:#10b981;
  --green-text:#1c9a78;
  --green-soft:#ecf7ee;
  --sky:#eaf3fd;
  --sky-2:#f1f7fe;
  --white:#ffffff;
  --grey:#8a93a6;
  --red:#e53e3e;
  --red-soft:#fde4e4;
  --star:#f5c518;
  --border:#dde8f6;
}
*{box-sizing:border-box;margin:0;padding:0}
html,body{width:1200px;height:1200px;overflow:hidden;background:var(--white)}
body{font-family:"Ubuntu",sans-serif;position:relative}
.site{position:absolute;left:498px;top:0;width:816px;height:4800px;transform:scale(.25);transform-origin:0 0;background:var(--sky);overflow:hidden}
section{position:relative;width:816px}
h2{color:var(--navy);font-weight:500;font-size:30px;text-align:center}
.lead{color:var(--green-text);font-size:12.5px;line-height:1.65;text-align:center;max-width:500px;margin:12px auto 0}
.card{position:absolute;background:var(--white);border-radius:12px;box-shadow:0 2px 10px rgba(31,54,168,.08)}
.card h3{color:var(--navy);font-weight:500;font-size:18px;line-height:1.25}
.card p{color:var(--green-text);font-size:10.5px;line-height:1.6}
.btn{display:inline-block;border-radius:20px;font-size:11px;padding:9px 20px;font-weight:500}
.btn-green{background:var(--green);color:var(--white)}
.btn-outline{border:2px solid #6b8ee8;color:var(--navy);background:var(--white)}

/* hero */
.hero{height:505px;text-align:center}
.hero-photo{position:absolute;inset:0;background:radial-gradient(ellipse at 45% 45%,#ffffff 0%,#e8f5ee 30%,#9fe0bd 65%,#cdeede 100%)}
.nav{position:absolute;left:16px;right:16px;top:20px;height:44px;background:var(--navy-deep);border-radius:10px;display:flex;align-items:center;padding:0 14px;color:var(--white)}
.brand{display:flex;align-items:center;gap:8px;font-size:11px;font-weight:500}
.brand-mark{width:26px;height:26px;background:var(--white);border-radius:6px}
.nav-links{display:flex;gap:10px;margin-left:auto;align-items:center;font-size:10px}
.nav-links span{padding:6px 10px;border-radius:8px}
.nav-links .active{background:rgba(255,255,255,.22)}
.nav-call{background:var(--green);border-radius:16px;padding:7px 14px !important;font-weight:500;margin-left:6px}
.hero-title{position:absolute;top:128px;left:0;right:0;font-size:52px;font-weight:700;color:var(--navy);line-height:1}
.hero-sub{position:absolute;top:240px;left:0;right:0;color:var(--green-text);font-size:20px;font-weight:500}
.hero-text{position:absolute;top:287px;left:0;right:0;color:var(--green-text);font-size:12px;line-height:1.7}
.hero-pill{position:absolute;top:352px;left:142px;width:532px;height:54px;background:var(--white);border-radius:12px;display:flex;align-items:center;justify-content:center;gap:8px;color:var(--navy);font-size:10.5px}
.hero-btns{position:absolute;top:432px;left:0;right:0;display:flex;justify-content:center;gap:16px}

/* why */
.why{height:664px;padding-top:52px}
.badge-line{color:var(--green-text);font-size:10px;text-align:center;margin-top:18px}
.feature{width:241px;padding:22px 20px}
.feature .t{display:flex;gap:8px;align-items:flex-start;justify-content:center;margin-bottom:18px}
.icon-dot{width:22px;height:22px;border-radius:50%;background:#e3ebfb;flex:none;margin-top:8px}

/* testimonials */
.reviews{height:353px;padding-top:50px}
.review{width:241px;height:182px;top:142px;padding:20px;text-align:center}
.stars{color:var(--star);font-size:14px;letter-spacing:1px}
.review q{display:block;color:var(--green-text);font-style:italic;font-size:10.5px;line-height:1.6;margin-top:10px}
.review .name{color:var(--navy);font-size:11px;margin-top:14px}
.review .role{color:var(--grey);font-size:9px;margin-top:3px}

/* process */
.process{height:821px;background:var(--green-soft);padding-top:45px}
.step{width:241px;padding:30px 18px;text-align:center}
.step .num{color:var(--navy);font-size:14px;font-weight:500;margin-bottom:22px}
.step h3{margin-bottom:8px}
.step .time{color:var(--green);font-size:8px;margin-top:10px}
.turnaround{left:182px;top:687px;width:452px;height:77px;display:flex;align-items:center;justify-content:center;gap:14px}
.turnaround b{display:block;color:var(--navy);font-weight:500;font-size:14px;text-align:center}
.turnaround span{color:var(--green-text);font-size:10px}

/* comparison */
.compare{height:525px;padding-top:55px}
.cmp{top:169px;width:382px;height:326px;padding:26px 24px}
.cmp-head{display:flex;gap:12px;align-items:flex-start;margin-bottom:16px}
.cmp ul{list-style:none}
.cmp li{display:flex;gap:8px;color:var(--green-text);font-size:10.5px;line-height:1.6;margin-bottom:10px}
.tick{flex:none;width:12px;height:12px;border:1.5px solid var(--green);border-radius:50%;margin-top:3px}
.bullet-red{flex:none;width:12px;height:12px;background:var(--red);border-radius:50%;margin-top:3px}
.cmp-bad{border:2px solid #f3a7ad}
.x-badge{width:28px;height:28px;border-radius:50%;background:var(--red-soft);color:var(--red);display:flex;align-items:center;justify-content:center;font-size:16px;flex:none}

/* design */
.design{height:535px;background:var(--sky-2)}
.design-col{position:absolute;left:6px;top:58px;width:385px}
.design-col h2{text-align:left;font-size:30px;line-height:1.25}
.design-col .lead{text-align:left;margin:16px 0 20px}
.design-col ul{list-style:none}
.design-col li{display:flex;gap:8px;color:var(--green-text);font-size:10.5px;margin-bottom:13px}
.tip{left:6px;top:410px;width:385px;height:95px;padding:22px 20px;color:var(--navy);font-size:10.5px;line-height:1.6}
.tip small{display:block;color:var(--green-text);font-size:9px;margin-top:4px}
.gallery-card{left:423px;top:189px;width:383px;height:174px;text-align:center;padding:36px 30px}
.gallery-card p{margin:12px 0 14px}

/* insurance */
.insurance{height:801px;background:var(--white);padding-top:55px}
.claims{left:28px;top:254px;width:380px;height:206px;padding:26px 20px}
.claims-head{display:flex;gap:12px;align-items:center;margin-bottom:14px}
.card-icon{width:36px;height:36px;border-radius:50%;background:#dfe8fb;flex:none;display:flex;align-items:center;justify-content:center}
.claims li{list-style:none;display:flex;gap:8px;color:var(--green-text);font-size:10px;margin-bottom:13px}
.check{color:var(--green);font-size:11px}
.gapfree{left:423px;top:171px;width:383px;height:368px;padding:26px 22px;border:1px solid var(--border)}
.gapfree .sub{margin:12px 0 18px}
.gapfree h4{color:var(--navy);font-weight:500;font-size:14px;margin:0 0 6px 10px}
.gapfree .tier{margin:0 0 26px 10px}
.gapfree strong{color:var(--green)}
.fine{color:var(--grey);font-style:italic;font-size:8.5px;line-height:1.6;margin-left:10px}
.divider{position:absolute;left:423px;top:568px;width:380px;height:2px;background:#e8edf5}
.funds-title{position:absolute;top:622px;left:0;right:0;text-align:center;color:var(--navy);font-weight:500;font-size:18px}
.funds{position:absolute;top:660px;left:114px;display:flex;gap:14px}
.fund{width:85px;height:85px;background:var(--white);border-radius:10px;box-shadow:0 2px 8px rgba(31,54,168,.1);display:flex;flex-direction:column;align-items:center;justify-content:center;gap:8px}
.fund-mark{width:32px;height:22px;border-radius:4px;background:#eef1f6}
.fund span{font-size:7.5px;color:var(--grey)}
.funds-note{position:absolute;top:772px;left:0;right:0;text-align:center;color:var(--green-text);font-size:10px}

/* cta */
.cta{height:373px;padding-top:68px;background:var(--sky-2)}
.stats{display:flex;justify-content:center;gap:110px;margin-top:28px;text-align:center}
.stats b{display:block;color:var(--green);font-size:18px;font-weight:500}
.stats span{color:var(--grey);font-size:8.5px}
.cta-btns{display:flex;justify-content:center;gap:14px;margin-top:24px}

/* footer */
.footer{height:223px;background:var(--sky-2);display:grid;grid-template-columns:205px 206px 205px 200px;padding:40px 0 0 6px}
.footer h5{color:var(--navy);font-weight:500;font-size:13px;margin-bottom:14px}
.footer p,.footer li{color:var(--green-text);font-size:9.5px;line-height:1.7;list-style:none}
.footer .links li{color:var(--grey)}
.footer .contact{color:var(--grey);margin-top:8px;display:flex;gap:6px;align-items:center}
.pin{width:8px;height:8px;border-radius:50%;background:var(--green);flex:none}
</style>
</head>
<body>
<main class="site">

  <section class="hero">
    <div class="hero-photo" role="img" aria-label="Close-up photo of a green and white custom sports mouthguard"></div>
    <nav class="nav">
      <div class="brand"><span class="brand-mark"></span>Tallow Mouthguards</div>
      <div class="nav-links">
        <span class="active">Home</span><span>About</span><span>Services</span><span>Gallery</span><span>Contact</span>
        <span class="nav-call">&#9990; (08) 6000 1234</span>
      </div>
    </nav>
    <h1 class="hero-title">TALLOW<br>MOUTHGUARDS</h1>
    <p class="hero-sub">Custom-Made Sports Mouthguards in Perth</p>
    <p class="hero-text">Protect your smile with a comfortable, professional fit designed by qualified<br>dental prosthetists with over 20 years experience.</p>
    <div class="hero-pill">
      <svg width="14" height="14" viewBox="0 0 24 24" fill="none" stroke="#10b981" stroke-width="2.5"><path d="M12 21s-8-5-8-11a4.5 4.5 0 0 1 8-2.8A4.5 4.5 0 0 1 20 10c0 6-8 11-8 11z"/></svg>
      Talk to us about our "gap free" mouthguards for eligible private health insurance members.
    </div>
    <div class="hero-btns"><span class="btn btn-green">Book Your Fitting Now</span><span class="btn btn-outline">Learn More About Us</span></div>
  </section>

  <section class="why">
    <h2>Why Choose Tallow Mouthguards?</h2>
    <p class="lead">Professional custom-fitted mouthguards designed by qualified dental prosthetists with over 20 years of experience in Perth, WA.</p>
    <p class="badge-line">&#9633; AdvDipDT DipDT Qualified • 20+ Years Experience • Locally Made in WA</p>

    <div class="card feature" style="left:28px;top:254px;height:187px"><div class="t"><h3>Professionally<br>Made</h3></div><p>Crafted by a qualified dental prosthetist (AdvDipDT DipDT) with over 20 years experience in the dental field.</p></div>
    <div class="card feature" style="left:288px;top:254px;height:187px"><div class="t"><h3>Custom<br>Precision Fit</h3></div><p>Designed for comfort, protection, and durability - custom made for your mouth providing precision fit.</p></div>
    <div class="card feature" style="left:547px;top:254px;height:187px"><div class="t"><h3>40+ Color<br>Designs</h3></div><p>Choose from nearly 40 colors with team colors, stripes, marbled effects, harlequin patterns, and glitter options.</p></div>

    <div class="card feature" style="left:28px;top:463px;height:167px"><div class="t"><span class="icon-dot"></span><h3>All Ages &amp;<br>Mobile Service</h3></div><p>Available for kids, teens, and adults with clinic and mobile school/club visits throughout Perth.</p></div>
    <div class="card feature" style="left:288px;top:463px;height:167px"><div class="t"><h3>Gap-Free<br>Insurance</h3></div><p>Gap-free mouthguards for eligible private health insurance members - we handle all claims processing.</p></div>
    <div class="card feature" style="left:547px;top:463px;height:167px"><div class="t"><span class="icon-dot"></span><h3>Fast Professional<br>Service</h3></div><p>Generally 1-2 weeks turnaround time, with express options available for urgent requirements.</p></div>
  </section>

  <section class="reviews">
    <h2>What Our Customers Say</h2>
    <div class="card review" style="left:28px"><div class="stars">★★★★★</div><q>The mobile clinic visit to our daughter's school was fantastic. Professional service and the kids loved choosing their colors!</q><div class="name">Hannah Reid</div><div class="role">Hockey Parent</div></div>
    <div class="card review" style="left:288px"><div class="stars">★★★★★</div><q>Tallow Mouthguards has been protecting our players for 3 seasons. Quality products and excellent service.</q><div class="name">Perth Falcons RFC</div><div class="role">Rugby Club</div></div>
    <div class="card review" style="left:547px"><div class="stars">★★★★★</div><q>Best mouthguard I've ever had. Comfortable, great protection, and looks professional. Highly recommend!</q><div class="name">Liam Carver</div><div class="role">Footy Player</div></div>
  </section>

  <section class="process">
    <h2>Simple 4-Step Process</h2>
    <p class="lead">Getting your custom mouthguard is easy. Our streamlined process ensures you get the perfect fit in just 1-2 weeks.</p>
    <div class="card step" style="left:28px;top:182px;height:226px"><div class="num">1</div><h3>Book Appointment</h3><p>Book an appointment at our Kelvale clinic or arrange a mobile visit to your school/sporting club</p><div class="time">5 minutes to book</div></div>
    <div class="card step" style="left:288px;top:182px;height:226px"><div class="num">2</div><h3>Take Impressions &amp;<br>Design</h3><p>Impressions are taken of your mouth (15 minutes) and you choose your colors and design style</p><div class="time">15 minute appointment</div></div>
    <div class="card step" style="left:547px;top:182px;height:226px"><div class="num">3</div><h3>Laboratory Creation</h3><p>Your mouthguard is professionally made in-house in our laboratory by our prosthetist and technicians</p><div class="time">1-2 week creation time</div></div>
    <div class="card step" style="left:28px;top:433px;height:201px"><div class="num">4</div><h3>Fit &amp; Collection</h3><p>Final fitting and collection from clinic, or packed delivery to schools/clubs - ready for game day!</p><div class="time">10 minutes final fitting</div></div>
    <div class="card turnaround">
      <svg width="16" height="16" viewBox="0 0 24 24" fill="none" stroke="#10b981" stroke-width="2.5"><circle cx="12" cy="12" r="9"/><path d="M12 7v5l3 2"/></svg>
      <div><b>Total Turnaround Time</b><span>Generally 1-2 weeks, with express options available for urgent requirements</span></div>
    </div>
  </section>

  <section class="compare">
    <h2>Custom vs Store-Bought Comparison</h2>
    <p class="lead">See why professional custom mouthguards provide superior protection compared to chemist alternatives.</p>
    <div class="card cmp" style="left:10px">
      <div class="cmp-head"><span class="tick" style="width:16px;height:16px;border-color:var(--navy);margin-top:6px"></span><h3>Professional Custom<br>Mouthguards</h3></div>
      <ul>
        <li><span class="tick"></span>Maximum Protection – absorbs impact and helps prevent broken teeth, jaw injuries, and concussions</li>
        <li><span class="tick"></span>Superior Comfort – designed to fit snugly, making it easier to breathe and talk while playing</li>
        <li><span class="tick"></span>Durability – crafted from high-quality dental materials that outlast off-the-shelf options</li>
        <li><span class="tick"></span>Precision fit for your unique mouth shape and bite</li>
        <li><span class="tick"></span>Professional design and manufacturing process</li>
        <li><span class="tick"></span>Nearly 40 color and design combinations available</li>
      </ul>
    </div>
    <div class="card cmp cmp-bad" style="left:423px">
      <div class="cmp-head" style="align-items:center"><span class="x-badge">✕</span><h3>Chemist "Boil &amp; Bite" Guards</h3></div>
      <ul>
        <li><span class="bullet-red"></span>Poor fit - one size fits none approach</li>
        <li><span class="bullet-red"></span>Limited protection against serious impacts</li>
        <li><span class="bullet-red"></span>Uncomfortable and bulky feeling</li>
        <li><span class="bullet-red"></span>Difficult to breathe and communicate clearly</li>
        <li><span class="bullet-red"></span>Cheap materials that wear out quickly</li>
        <li><span class="bullet-red"></span>Very limited color and design options</li>
      </ul>
    </div>
  </section>

  <section class="design">
    <div class="design-col">
      <h2>Design Your Perfect<br>Mouthguard</h2>
      <p class="lead">Choose from nearly 40 colors and mix them into different styles. All locally made right here in Western Australia.</p>
      <ul>
        <li><span class="tick"></span>Team colors and club designs</li>
        <li><span class="tick"></span>Stripes and geometric patterns</li>
        <li><span class="tick"></span>Marbled and gradient effects</li>
        <li><span class="tick"></span>Harlequin and diamond patterns</li>
        <li><span class="tick"></span>Glitter overlay on any color</li>
        <li><span class="tick"></span>Custom names and numbers</li>
        <li><span class="tick"></span>Locally made in Western Australia</li>
      </ul>
    </div>
    <div class="card tip"><b>Pro Tip:</b> If you have your colours and a style in mind before your appointment with us you are one step ahead!<small>View the full range at <b>www.customguardrange.com</b></small></div>
    <div class="card gallery-card"><h3>See Our Work</h3><p>Browse our gallery to see the quality and variety of custom mouthguards we create.</p><span class="btn btn-green">View Gallery</span></div>
  </section>

  <section class="insurance">
    <h2>Insurance Claims Made Easy</h2>
    <p class="lead">We use Morvex for seamless private health insurance claims processing, making your gap-free mouthguard experience effortless.</p>
    <div class="card claims">
      <div class="claims-head"><span class="card-icon"><svg width="16" height="12" viewBox="0 0 16 12"><rect width="16" height="12" rx="2" fill="#2236b0"/><rect y="4" width="16" height="2" fill="#fff"/></svg></span><div><h3>Instant Claims Processing</h3><p>Professional health fund integration</p></div></div>
      <ul>
        <li><span class="check">✓</span>On-the-spot claims processing at time of service</li>
        <li><span class="check">✓</span>Works with all major private health funds</li>
        <li><span class="check">✓</span>Secure electronic claiming system</li>
        <li><span class="check">✓</span>Immediate benefit calculation and payment</li>
      </ul>
    </div>
    <div class="card gapfree">
      <div style="display:flex;gap:10px;align-items:center"><svg width="14" height="14" viewBox="0 0 24 24" fill="none" stroke="#2236b0" stroke-width="2.5"><path d="M12 21s-8-5-8-11a4.5 4.5 0 0 1 8-2.8A4.5 4.5 0 0 1 20 10c0 6-8 11-8 11z"/></svg><h3>Gap-Free Mouthguards</h3></div>
      <p class="sub">We're pleased to offer "gap free" mouthguards to private health members with dental coverage.</p>
      <h4>Single &amp; Double Layer</h4>
      <p class="tier"><strong>100% covered</strong> by private health insurance with dental benefits</p>
      <h4>Triple Layer</h4>
      <p class="tier">May incur a <strong>small gap payment</strong> for maximum protection</p>
      <p class="fine">* Check your policy details to ensure mouthguard coverage is included. We'll verify your benefits before treatment.</p>
    </div>
    <div class="divider"></div>
    <div class="funds-title">Accepted Health Funds</div>
    <div class="funds">
      <div class="fund"><span class="fund-mark"></span><span>Coralwell</span></div>
      <div class="fund"><span class="fund-mark"></span><span>Brightfund</span></div>
      <div class="fund"><span class="fund-mark"></span><span>Harbourcare</span></div>
      <div class="fund"><span class="fund-mark"></span><span>Northway</span></div>
      <div class="fund"><span class="fund-mark"></span><span>Crestline</span></div>
      <div class="fund"><span class="fund-mark"></span><span>Westhaven</span></div>
    </div>
    <p class="funds-note">And many more! Contact us to verify your specific fund coverage.</p>
  </section>

  <section class="cta">
    <h2>Ready to Protect Your Smile?</h2>
    <p class="lead">Join thousands of satisfied athletes across Perth. Book your custom mouthguard fitting today - mobile visits available for schools and sporting clubs.</p>
    <div class="stats">
      <div><b>20+</b><span>Years Experience</span></div>
      <div><b>1000+</b><span>Happy Athletes</span></div>
      <div><b>100+</b><span>Schools &amp; Clubs</span></div>
    </div>
    <div class="cta-btns"><span class="btn btn-green">Call (08) 6000 1234</span><span class="btn btn-outline">Book Online Now</span></div>
  </section>

  <footer class="footer">
    <div>
      <h5>Tallow Mouthguards</h5>
      <p>Professional custom-fitted sports mouthguards designed by qualified dental prosthetists in Perth, WA.</p>
      <p class="contact"><span class="pin"></span>(08) 6000 1234</p>
      <p class="contact" style="margin-top:2px"><span class="pin"></span>hello@tallowmouthguards.com.au</p>
    </div>
    <div class="links"><h5>Quick Links</h5><ul><li>Home</li><li>About Us</li><li>Our Services</li><li>Gallery</li><li>Contact</li></ul></div>
    <div class="links"><h5>Services</h5><ul><li>Custom Mouthguards</li><li>Mobile Clinic Visits</li><li>School Group Bookings</li><li>Sports Club Visits</li><li>Insurance Claims</li></ul></div>
    <div class="links">
      <h5>Visit Us</h5>
      <p class="contact" style="margin-top:0;align-items:flex-start"><span class="pin" style="margin-top:4px"></span>Unit 5, 14 Harbour Crescent,<br>Kelvale, Western Australia, 6000</p>
      <p class="contact" style="align-items:flex-start"><span class="pin" style="margin-top:4px"></span>Mon-Fri: 9:00 AM - 5:00 PM<br>Sat: 9:00 AM - 1:00 PM<br>Sun: Closed</p>
    </div>
  </footer>

</main>
</body>
</html>
```